New Zealand Export company needs business cards

We need new business cards to match our new logo for a company based in New Zealand who deal specifically with the Pacific Islands. We source, consolidate and ship products out of New Zealand to the Pacific Islands. Will attach our old ones and also new logo.
Would like the Islands we deal with and the areas of work we have access to, to be included on the business cards.

Contact Information for Business Card

T +64 9 571 3048
F +64 9 571 6285
12-18 Kowhai Lane, Ferngate, 2190
PO Box 814, Ferngate, Auckland 2295, New Zealand
www.falconfreight.example.nz
E sales@falconfreight.example.nz

Font styles to use
Sans Serif

Colors
85abd2
33a6d7
ffffff

Requirements
Must have
• A company of PWM

```html
<!DOCTYPE html>
<html lang="en">
<head>
<meta charset="utf-8">
<title>Falcon Freight – Business Cards</title>
<link rel="stylesheet" href="https://fonts.googleapis.com/css2?family=Play:wght@400;700&display=swap">
<style>
  :root {
    --backdrop: #6a6a6a;
    --brand-blue: #1c5a9e;
    --brand-cyan: #33a6d7;
    --card-white: #ffffff;
    --card-black: #1a1a1a;
    --ink-blue: #1d4f8a;
  }
  * { box-sizing: border-box; margin: 0; padding: 0; }
  html, body {
    width: 1200px; height: 800px; overflow: hidden;
    background: var(--backdrop);
    font-family: "Play", "Trebuchet MS", sans-serif;
  }
  .stage { position: relative; width: 1200px; height: 800px; }

  .card {
    position: absolute;
    width: 580px; height: 330px;
    box-shadow: 0 10px 24px rgba(0,0,0,0.3);
    overflow: hidden;
  }

  /* Front card */
  .card-front { left: 580px; top: 60px; display: flex; background: var(--card-white); }
  .front-identity {
    width: 324px; height: 100%;
    background: var(--brand-blue);
    color: var(--card-white);
    display: flex; flex-direction: column; align-items: center; justify-content: center;
    text-align: center;
  }
  .person-name { font-size: 28px; font-weight: 700; letter-spacing: 3px; }
  .person-role { font-size: 15px; letter-spacing: 1px; margin-top: 4px; }

  .front-details {
    flex: 1; padding: 50px 16px 28px 22px;
    display: flex; flex-direction: column; justify-content: space-between;
  }
  .brand-name {
    display: flex; align-items: center; gap: 8px;
    color: var(--brand-blue); font-weight: 700; letter-spacing: 1px;
  }
  .brand-square { width: 14px; height: 14px; background: var(--brand-cyan); flex: none; }
  .front-details .brand-name { font-size: 22px; line-height: 1.05; justify-content: center; }

  .contact-group { display: flex; gap: 10px; align-items: flex-start; margin-top: 12px; }
  .contact-icon { width: 20px; height: 20px; flex: none; margin-top: 1px; }
  .contact-lines { color: var(--ink-blue); font-size: 11.5px; line-height: 1.55; font-weight: 700; white-space: nowrap; }
  .contact-lines .label { display: inline-block; width: 16px; }

  /* Back card */
  .card-back {
    left: 40px; top: 420px;
    background: var(--card-black);
    display: flex; flex-direction: column; align-items: center; justify-content: center;
    text-align: center;
  }
  .card-back .brand-name { font-size: 30px; color: var(--brand-blue); }
  .back-rule { width: 60px; height: 2px; background: var(--brand-cyan); margin: 34px 0 14px; }
  .back-address { color: var(--brand-cyan); font-size: 12.5px; line-height: 1.6; letter-spacing: 0.3px; }
</style>
</head>
<body>
<main class="stage">

  <section class="card card-back" aria-label="Business card back">
    <div class="brand-name"><span class="brand-square"></span>FALCON FREIGHT</div>
    <div class="back-rule"></div>
    <p class="back-address">
      12-18 Kowhai Lane, Ferngate, 2190 PO Box 814, Ferngate,<br>
      Auckland 2295, New Zealand
    </p>
  </section>

  <section class="card card-front" aria-label="Business card front">
    <div class="front-identity">
      <div class="person-name">TESS HARLOW</div>
      <div class="person-role">Sales Manager</div>
    </div>
    <div class="front-details">
      <div class="brand-name"><span class="brand-square"></span>FALCON<br>FREIGHT</div>
      <div class="contact-list">
        <div class="contact-group">
          <svg class="contact-icon" viewBox="0 0 20 20" aria-hidden="true">
            <path d="M3 8 Q10 3 17 8 L15 10 L13 8 L7 8 L5 10 Z" fill="var(--brand-cyan)"/>
            <rect x="4" y="10" width="12" height="7" rx="1.5" fill="var(--brand-cyan)"/>
            <circle cx="10" cy="13.5" r="2" fill="var(--card-white)"/>
          </svg>
          <div class="contact-lines">
            <div><span class="label">T</span>+64 9 571 3048</div>
            <div><span class="label">F</span>+64 9 571 6285</div>
          </div>
        </div>
        <div class="contact-group">
          <svg class="contact-icon" viewBox="0 0 20 20" aria-hidden="true" fill="none" stroke="var(--brand-cyan)" stroke-width="1.4">
            <circle cx="10" cy="10" r="8"/>
            <ellipse cx="10" cy="10" rx="3.5" ry="8"/>
            <line x1="2" y1="10" x2="18" y2="10"/>
            <line x1="3.5" y1="6" x2="16.5" y2="6"/>
            <line x1="3.5" y1="14" x2="16.5" y2="14"/>
          </svg>
          <div class="contact-lines">
            <div><span class="label">W</span>www.falconfreight.example.nz</div>
            <div><span class="label">E</span>sales@falconfreight.example.nz</div>
          </div>
        </div>
      </div>
    </div>
  </section>

</main>
</body>
</html>
```